5 CD Designs for 5 albums soon on tunevault and brindle music

I'm looking for something fairly unique, i make music shameless plug: www.wavecrate.net/tidalmoth and i'm looking for 5 EP covers. 4 of my EP's are allready listed called:

Glass & Ember
Reed & Salt
Hollow & Frost

and i'm working on a new one in the next month.

I'm looking for a unique design style that matches the music but also something that carries that same style across the 5 designs.

Now i know exposure doesn't pay the bills but i promise to give credit as much as i can, i'm also looking for someone who could keep providing artwork for the albums of the future

Font styles to use
Decorative
Script

Colors
ffffff
85cae6
0692cd

Requirements
Must have
• 5 unique designs
Nice to have
• a nominalistic representation of the music

```html
<!DOCTYPE html>
<html lang="en">
<head>
<meta charset="utf-8">
<title>Glass &amp; Ember / Reed &amp; Salt — EP covers</title>
<link rel="stylesheet" href="https://fonts.googleapis.com/css2?family=Monoton&family=Josefin+Sans:wght@200;300&display=swap">
<style>
  :root {
    --sheet: #ecebe6;
    --paper-white: #ffffff;
    --paper-cream: #efede3;
    --paper-ice: #eaf8fd;
    --olive: #4f5030;
    --olive-soft: #7c8572;
    --olive-haze: rgba(170, 178, 150, .22);
    --blue: #0692cd;
    --blue-soft: #85cae6;
    --blue-haze: rgba(133, 202, 230, .22);
    --tape-dark: #3f4033;
    --tape-mid: #6b6c5a;
  }
  * { box-sizing: border-box; margin: 0; padding: 0; }
  html, body { width: 1200px; height: 1200px; overflow: hidden; background: var(--sheet); }
  .sheet { position: relative; width: 1200px; height: 1200px; }

  .cover {
    position: absolute; width: 574px; height: 574px; overflow: hidden;
    box-shadow: 0 2px 5px rgba(0,0,0,.25);
  }
  .cover--tl { left: 13px;  top: 13px; }
  .cover--tr { left: 605px; top: 13px; }
  .cover--bl { left: 13px;  top: 605px; }
  .cover--br { left: 605px; top: 605px; }

  .cover--white { background: var(--paper-white); }
  .cover--cream { background: var(--paper-cream); }
  .cover--ice   { background: var(--paper-ice); }

  .wave-haze {
    position: absolute; left: 0; top: 10px; width: 574px; height: 230px;
  }
  .theme-olive .wave-haze {
    background: radial-gradient(ellipse 70% 45% at 50% 55%, var(--olive-haze) 0%, rgba(255,255,255,0) 100%);
  }
  .theme-blue .wave-haze {
    background: radial-gradient(ellipse 70% 45% at 50% 55%, var(--blue-haze) 0%, rgba(255,255,255,0) 100%);
  }

  .ep-title {
    position: absolute; left: 0; right: 0; top: 74px; text-align: center;
    font-family: "Monoton", "Josefin Sans", sans-serif; font-weight: 400; font-size: 46px;
    line-height: 60px; letter-spacing: 1px; white-space: nowrap;
  }
  .ep-title .amp { font-family: "Josefin Sans", sans-serif; font-weight: 200; font-size: 48px; margin: 0 6px; }
  .theme-olive .ep-title { color: var(--olive-soft); }
  .theme-blue  .ep-title { color: var(--blue); }

  .tape-art {
    position: absolute; left: 106px; top: 214px; width: 372px; height: 114px;
    border-radius: 48% 52% 30% 30% / 60% 60% 40% 40%;
    background: radial-gradient(ellipse at 50% 45%, var(--tape-mid) 0%, var(--tape-dark) 70%, rgba(63,64,51,0) 100%);
    box-shadow: 0 14px 14px -8px rgba(0,0,0,.3);
  }
  .orb-band {
    position: absolute; left: 0; top: 211px; width: 574px; height: 124px;
    background: linear-gradient(90deg,
      rgba(133,202,230,.75) 0%, rgba(6,146,205,.55) 15%, rgba(133,202,230,.45) 35%,
      rgba(6,146,205,.6) 55%, rgba(133,202,230,.5) 75%, rgba(6,146,205,.5) 100%);
    border-radius: 60px;
    -webkit-mask-image: linear-gradient(180deg, transparent 0%, #000 25%, #000 75%, transparent 100%);
            mask-image: linear-gradient(180deg, transparent 0%, #000 25%, #000 75%, transparent 100%);
  }

  .label-lockup {
    position: absolute; left: 116px; top: 400px; height: 120px;
    display: flex; align-items: center; gap: 18px;
  }
  .label-name {
    font-family: "Josefin Sans", sans-serif; font-weight: 300; font-size: 38px;
    letter-spacing: 1px; text-transform: uppercase; line-height: 1;
  }
  .label-ring {
    width: 120px; height: 120px; border-radius: 50%; border: 1.2px solid currentColor;
  }
  .theme-olive .label-lockup { color: var(--olive); }
  .theme-blue  .label-lockup { color: var(--blue); }
</style>
</head>
<body>
<main class="sheet">

  <section class="cover cover--tl cover--white theme-olive">
    <div class="wave-haze" role="img" aria-label="Faint sweeping bundle of fine wavy lines"></div>
    <h2 class="ep-title">GLASS<span class="amp">&amp;</span>EMBER</h2>
    <div class="tape-art" role="img" aria-label="Photograph of a tangled pile of loose cassette tape"></div>
    <div class="label-lockup"><p class="label-name">tidalmoth</p><span class="label-ring"></span></div>
  </section>

  <section class="cover cover--tr cover--cream theme-olive">
    <div class="wave-haze" role="img" aria-label="Faint sweeping bundle of fine wavy lines"></div>
    <h2 class="ep-title">GLASS<span class="amp">&amp;</span>EMBER</h2>
    <div class="tape-art" role="img" aria-label="Photograph of a tangled pile of loose cassette tape"></div>
    <div class="label-lockup"><p class="label-name">tidalmoth</p><span class="label-ring"></span></div>
  </section>

  <section class="cover cover--bl cover--ice theme-blue">
    <div class="wave-haze" role="img" aria-label="Faint sweeping bundle of fine wavy lines"></div>
    <h2 class="ep-title">REED<span class="amp">&amp;</span>SALT</h2>
    <div class="orb-band" role="img" aria-label="Band of overlapping translucent blue circles like bokeh light"></div>
    <div class="label-lockup"><p class="label-name">tidalmoth</p><span class="label-ring"></span></div>
  </section>

  <section class="cover cover--br cover--white theme-blue">
    <div class="wave-haze" role="img" aria-label="Faint sweeping bundle of fine wavy lines"></div>
    <h2 class="ep-title">REED<span class="amp">&amp;</span>SALT</h2>
    <div class="orb-band" role="img" aria-label="Band of overlapping translucent blue circles like bokeh light"></div>
    <div class="label-lockup"><p class="label-name">tidalmoth</p><span class="label-ring"></span></div>
  </section>

</main>
</body>
</html>
```